ALL TEXT Social Media Graphics

We are looking for a series of social media graphics for Instagram (new size: 4:5 (1080 x 1350 pixels) ratio that are ALL TEXT. We want the following quotes below on each graphic; one quote per graphic. AND, In very small letters at the bottom of each graphic, add @PaulaWrenLive
The look and feel of these graphics should be complimentary to the color palette attached below; but keep them simple. But the design is up to you; at the end of this document, I provided various samples of all text graphics that I like as examples.
The Quotes are in the attached WORD document
women trying to lose weight

```html
<!DOCTYPE html>
<html lang="en">
<head>
<meta charset="utf-8">
<title>Golden Summer Slimdown – Social Graphics</title>
<link href="https://fonts.googleapis.com/css2?family=Barlow+Semi+Condensed:wght@600&family=Barlow:wght@300;600&family=Quicksand:wght@700&display=swap" rel="stylesheet">
<style>
  :root{
    --page:#d3d3d3;
    --ink:#a3124e;
    --accent:#e9579b;
    --cta:#e66aa3;
    --card-top:#ffffff;
    --card-bottom:#fdecf4;
  }
  *{margin:0;padding:0;box-sizing:border-box}
  html,body{width:1200px;height:611px;overflow:hidden;background:var(--page)}
  .board{position:relative;width:1200px;height:611px}
  .post{
    position:absolute;width:224px;height:280px;
    background:linear-gradient(160deg,var(--card-top) 35%,var(--card-bottom) 100%);
    color:var(--ink);
  }
  .post__hook{
    position:absolute;left:16px;right:8px;
    font-family:"Barlow Semi Condensed",sans-serif;font-weight:600;
    font-size:17px;line-height:20.8px;letter-spacing:-0.2px;
  }
  .post__promise{
    position:absolute;left:16px;right:4px;
    font-family:"Quicksand",sans-serif;font-weight:700;
    font-size:19px;line-height:22.4px;letter-spacing:-0.2px;
  }
  .post__cta{
    position:absolute;left:16px;right:8px;
    font-family:"Barlow",sans-serif;font-weight:300;
    font-size:12px;line-height:14.6px;color:var(--cta);
  }
  .post__cta b{font-weight:600;color:var(--ink)}
  .post__handle{
    position:absolute;left:17px;top:253px;
    font-family:"Barlow",sans-serif;font-weight:600;font-size:6.5px;color:var(--ink);
  }
  .post__marker{position:absolute;left:0;top:250px;width:7px;height:13px;background:var(--accent)}
  .accent{color:var(--accent)}
</style>
</head>
<body>
<main class="board">

  <article class="post" style="left:19px;top:20px">
    <p class="post__hook" style="top:26px">You Can Absolutely<br>Be Down <span class="accent">20–30</span> Pounds<br>By End Of Summer.</p>
    <p class="post__promise" style="top:113px">All It Takes Is <span class="accent">The<br>Right Plan</span>—and<br>You’ve Found It.</p>
    <p class="post__cta" style="top:209px">Comment “<b>GOLDEN</b>” For The<br>Golden Summer Slimdown!</p>
    <span class="post__marker"></span><span class="post__handle">@PaulaWrenLive</span>
  </article>

  <article class="post" style="left:254px;top:20px">
    <p class="post__hook" style="top:26px">You <span class="accent">Don’t Need</span><br>Another Diet—You Need<br>A System That Works.</p>
    <p class="post__promise" style="top:113px">Drop <span class="accent">30 Pounds</span><br>With The Golden<br>Summer Slimdown.</p>
    <p class="post__cta" style="top:212px">Comment “<b>SUMMER</b>”<br>To Start Now.</p>
    <span class="post__marker"></span><span class="post__handle">@PaulaWrenLive</span>
  </article>

  <article class="post" style="left:489px;top:20px">
    <p class="post__hook" style="top:28px">This <span class="accent">Summer Ain’t<br>Over</span>—and Neither<br>Are Your Body Goals.</p>
    <p class="post__promise" style="top:113px">Drop 30 Pounds<br>With <span class="accent">The Golden</span><br>Summer Slimdown.</p>
    <p class="post__cta" style="top:209px">Comment “<b>GOLDEN</b>”<br>To Get The Plan</p>
    <span class="post__marker"></span><span class="post__handle">@PaulaWrenLive</span>
  </article>

  <article class="post" style="left:724px;top:20px">
    <p class="post__hook" style="top:29px">If Your Goal is<br>a Tiny Waist, Flat<br>Belly, and</p>
    <p class="post__promise" style="top:109px"><span class="accent">30 Pounds</span><br>Down. This is<br>the plan.</p>
    <p class="post__cta" style="top:192px">Comment “<b>SUMMER</b>” To<br>Join The Golden<br>Summer Slimdown!</p>
    <span class="post__marker"></span><span class="post__handle">@PaulaWrenLive</span>
  </article>

  <article class="post" style="left:959px;top:20px">
    <p class="post__hook" style="top:29px">There’s Still Time<br>To Drop The <span class="accent">30 Pounds</span><br>And slay This Summer.</p>
    <p class="post__promise" style="top:109px">The <span class="accent">Golden<br>Summer</span> Slimdown<br>Has The Blue Print</p>
    <p class="post__cta" style="top:213px">Comment “<b>GOLDEN</b>”!</p>
    <span class="post__marker"></span><span class="post__handle">@PaulaWrenLive</span>
  </article>

  <article class="post" style="left:19px;top:311px">
    <p class="post__hook" style="top:29px">Snatched Waist,<br>Flat Tummy,<br><span class="accent">30 Pounds</span> Lighter</p>
    <p class="post__promise" style="top:107px">That’s <span class="accent">What The<br>Golden</span> Summer<br>Slimdown Challenge<br>Delivers.</p>
    <p class="post__cta" style="top:213px">COMMENT “<b>GOLDEN</b>”<br>TO GET THE PLAN</p>
    <span class="post__marker"></span><span class="post__handle">@PaulaWrenLive</span>
  </article>

  <article class="post" style="left:254px;top:311px">
    <p class="post__hook" style="top:29px">Nothing <span class="accent">feels better</span><br>than seeing that <span class="accent">scale<br>drop</span> week after week.</p>
    <p class="post__promise" style="top:109px">Let’s <span class="accent">lose up to<br>30 pounds</span> this<br>summer—together.</p>
    <p class="post__cta" style="top:198px">Comment “<b>SUMMER</b>”<br>to Join The Golden<br>Summer Slim Down!</p>
    <span class="post__marker"></span><span class="post__handle">@PaulaWrenLive</span>
  </article>

  <article class="post" style="left:489px;top:311px">
    <p class="post__hook" style="top:29px">Sis, <span class="accent">we’re<br>dropping</span> belly<br>fat and</p>
    <p class="post__promise" style="top:109px">saying <span class="accent">goodbye<br>to stubborn</span><br>pounds.</p>
    <p class="post__cta" style="top:198px;left:15px">Join The Golden<br>Summer Slimdown<br>Comment “<b>Summer</b>”!</p>
    <span class="post__marker"></span><span class="post__handle">@PaulaWrenLive</span>
  </article>

  <article class="post" style="left:724px;top:311px">
    <p class="post__hook" style="top:28px">Don’t <span class="accent">wait<br>‘til next</span> summer<br>to get right.</p>
    <p class="post__promise" style="top:104px">The time is NOW.<br><span class="accent">Drop 30 pounds</span><br>with the Golden<br>Summer Slimdown.</p>
    <p class="post__cta" style="top:224px">Comment “<b>Summer</b>”!</p>
    <span class="post__marker"></span><span class="post__handle">@PaulaWrenLive</span>
  </article>

  <article class="post" style="left:959px;top:311px">
    <p class="post__hook" style="top:28px">You’ve got <span class="accent">8 weeks</span><br>and the perfect plan<br>to <span class="accent">drop 30 pounds</span>.</p>
    <p class="post__promise" style="top:104px">Let’s <span class="accent">get snatched<br>this summer</span> with<br>the Golden<br>Summer Slimdown.</p>
    <p class="post__cta" style="top:227px">Comment “<b>Summer</b>”!</p>
    <span class="post__marker"></span><span class="post__handle">@PaulaWrenLive</span>
  </article>

</main>
</body>
</html>
```